Website design for Cambridge based systematic hedge fund

We have run previous craftmosaic competitions to design our company logo, business cards and the styling of our presentation deck (see attached files).
As the final step we are looking to get a website designed that is thematically consistent with these existing elements of our branding.
You can find some of our competitors websites below:
https://www.quelmarsh.example/
https://www.fenloor.example/
https://www.pyvart.example/
https://www.dulvet.example/
https://www.orbelmfunds.example/
https://www.valtrigo.example/
https://www.meskilfunds.example/home
We would like to have a website that works well on both mobile devices and desktops. Either just as one page that can be scrolled down, with links at the top that skips to certain sections, or a few separate pages that can be navigated by a top menu.
It should look professional, we are not after lots of animations or unnecessary transitions, and in particular the website must be smooth to navigate. We would like to avoid having peoples of people, we are happy to make use of elements from the presentation (for example the style of the cover slide, or the section slides with the faded bridge in the background), or 'financial' style images.
We would like to have the following sections for now. For some of these some example text has been provided, final text may change but it will be of similar length. For the other sections we are happy to just have template text for now. At the moment we are mainly interested to see styles/layouts as words can be added easily afterwards:
1) We will need a disclaimer pop up the first time someone visits the site (see for example the meskilfunds example).
2) Top page - company name, then in larger text "Bringing AI and Statistical Inference to Financial Markets", and somewhere in smaller text "Harlow Vectors is a quantitative asset manager with the singular focus of delivering algorithmic strategies that work"
3) "About us" section: will describe us as a company, details our approach, company values, and explains the company logo.
Example text:
"We deliver consistent alpha across liquid markets through the application of proprietary IP in Bayesian inference, machine learning and artificial intelligence. We are a multi-disciplinary team founded by experienced finance professionals from premier institutions, leading academics from the Thornbury Stellar Unit at Ashmere College and world-class software engineers.
Our logo portrays a sillhoute of the lattice walkway at Ashmere College. Our unique scientific approach allows us to bridge cutting-edge mathematical research and computing expertise with financial knowledge to bring algorithmns that work to liquid markets"
4) Hiring section, detailing our culture, what we are looking for.
Example text:
"We are always looking for exceptional talent to join our entrepreneurial team. We are looking for individuals who are creative thinkers, can demonstrate analytical rigour and are passionate about the intersection of science, finance and technology.
We prioritise having a company culture that promotes sharing ideas in a safe, collaborative research environment. We make sure that every member of the team has the oppertunity to explore their own ideas through weekly 'innovation time', and ensure that everyone gets the support they need to continue to grow as individuals within the company."
5) A section for news/press releases
6) Contact us area at the bottom with office location and email. We will need to list 3 addresses for our Cambridge, London and Singapore offices, along with a couple of contact emails or phone numbers
7) A client login button at the top that will take them to a different website (unrelated to this one).

```html
<!DOCTYPE html>
<html lang="en">
<head>
<meta charset="utf-8">
<title>Harlow Vectors</title>
<link href="https://fonts.googleapis.com/css2?family=Fira+Sans:wght@400;500;600;700&family=Roboto:wght@400;500&display=swap" rel="stylesheet">
<style>
:root{
  --ink:#1f2429;
  --navy:#133152;
  --blue:#0d3e6e;
  --accent:#0c4a85;
  --text:#222831;
  --muted:#7d858d;
  --line:#e6e9ed;
  --field:#f7f8fa;
  --paper:#ffffff;
  --soft:#f4f5f7;
}
*{box-sizing:border-box;margin:0;padding:0}
html,body{width:1200px;height:3158px;overflow:hidden}
body{position:relative;background:var(--paper);font-family:"Roboto",Arial,sans-serif;color:var(--text)}

/* top bar */
.topbar{position:absolute;left:0;top:0;width:1200px;height:60px;background:var(--ink)}
.contact-item{position:absolute;top:18px;display:flex;gap:10px;align-items:flex-start;color:#fff;font-family:"Fira Sans",Arial,sans-serif}
.contact-item .ico{width:22px;height:22px;background:var(--accent);border-radius:3px;display:flex;align-items:center;justify-content:center;font-size:11px;font-weight:600;color:#fff;margin-top:2px}
.contact-item b{display:block;font-size:9.5px;font-weight:600}
.contact-item span{display:block;font-size:9px;color:#a9b2bc;margin-top:1px}
.client-login{position:absolute;left:923px;top:0;width:115px;height:60px;background:var(--blue);color:#fff;font:600 11px "Fira Sans",Arial,sans-serif;display:flex;align-items:center;justify-content:center;gap:7px}

/* header */
.header{position:absolute;left:0;top:60px;width:1200px;height:90px;background:#fff}
.brand{position:absolute;left:161px;top:30px;display:flex;align-items:center;gap:9px;font:700 20px "Fira Sans",Arial,sans-serif;color:var(--blue)}
.brand i{width:14px;height:14px;background:var(--blue);display:block}
.nav{position:absolute;right:162px;top:38px;display:flex;gap:20px;font:600 11px "Fira Sans",Arial,sans-serif;color:var(--navy)}

/* hero */
.hero{position:absolute;left:0;top:150px;width:1200px;height:424px;background:var(--navy);overflow:hidden}
.hero-net{position:absolute;right:0;top:0;width:600px;height:424px;background:radial-gradient(ellipse at 75% 45%,rgba(120,150,185,.28),rgba(19,49,82,0) 65%)}
.hero h1{position:absolute;left:161px;top:26px;width:420px;font:700 51px/56px "Fira Sans",Arial,sans-serif;color:#fff}
.hero p{position:absolute;left:161px;top:268px;width:440px;font-size:13.5px;line-height:20px;color:#dfe6ee}
.btn{position:absolute;display:flex;align-items:center;justify-content:center;gap:7px;font:600 11px "Fira Sans",Arial,sans-serif}
.btn-dark{background:var(--blue);color:#fff}
.btn-light{background:#fff;color:var(--navy)}
.vertical-url{position:absolute;left:1168px;top:60px;writing-mode:vertical-rl;transform:rotate(180deg);font-size:9px;letter-spacing:3.5px;color:#6f86a0;height:290px;text-align:center}

/* feature rows */
.photo{position:absolute;box-shadow:0 10px 25px rgba(0,0,0,.18)}
.kicker{position:absolute;font-size:10px;color:var(--accent)}
.title{position:absolute;font:500 29px "Fira Sans",Arial,sans-serif;color:var(--text)}
.dash{position:absolute;width:14px;height:4px;border-top:1px solid var(--accent);border-bottom:1px solid var(--accent)}
.copy{position:absolute;width:428px;font-size:10.4px;line-height:15.8px;color:var(--muted)}
.copy p+p{margin-top:10px}

/* press */
.press{position:absolute;left:0;top:1450px;width:1200px;height:609px;background:var(--blue);overflow:hidden}
.press-net{position:absolute;right:0;top:0;width:520px;height:609px;background:radial-gradient(ellipse at 80% 40%,rgba(120,160,200,.22),rgba(13,62,110,0) 65%)}
.press .kicker{color:#fff;width:1200px;text-align:center;top:74px}
.press h2{position:absolute;top:96px;width:1200px;text-align:center;font:500 29px "Fira Sans",Arial,sans-serif;color:#fff}
.card-img{position:absolute;top:179px;width:278px;height:298px}
.card{position:absolute;top:396px;width:217px;height:138px;background:#fff;text-align:center}
.card h3{margin-top:22px;font:500 16px "Fira Sans",Arial,sans-serif;color:var(--text)}
.card time{display:block;margin-top:4px;font-size:10px;color:var(--muted)}
.shares{display:flex;gap:12px;justify-content:center;margin-top:16px}
.shares span{width:18px;height:18px;border:1px solid var(--line);display:block}

/* contact form */
.section-label{position:absolute;top:2133px;width:1200px;text-align:center;font-size:10.5px;color:var(--accent)}
.section-label:before,.section-label:after{content:"";display:inline-block;width:8px;height:3px;border-top:1px solid var(--accent);border-bottom:1px solid var(--accent);margin:0 12px;vertical-align:middle}
.contact-title{position:absolute;top:2156px;width:1200px;text-align:center;font:500 29px "Fira Sans",Arial,sans-serif}
.field{position:absolute;background:var(--field);border:1px solid #eef0f3;font-size:10.5px;color:var(--muted);padding:12px 14px}
.field.select{color:var(--text);display:flex;justify-content:space-between}

/* cta band */
.cta{position:absolute;left:0;top:2654px;width:1200px;height:112px;background:var(--blue)}
.cta h2{position:absolute;left:161px;top:43px;font:600 20px "Fira Sans",Arial,sans-serif;color:#fff}
.cta .btn{left:898px;top:38px;width:140px;height:38px;background:var(--ink);color:#fff}

/* offices */
.offices{position:absolute;left:0;top:2766px;width:1200px;height:392px;background:var(--soft)}
.office{position:absolute;top:55px;width:240px;text-align:center}
.pin{width:59px;height:59px;border-radius:50%;background:#fff;margin:0 auto;display:flex;align-items:center;justify-content:center}
.office h3{margin-top:27px;font:500 16px "Fira Sans",Arial,sans-serif}
.office p{margin-top:10px;font-size:10.4px;line-height:15.8px;color:var(--muted)}
.rule{position:absolute;left:161px;top:304px;width:877px;height:1px;background:#e4e7eb}
.copyright{position:absolute;left:161px;top:337px;font-size:11px;color:var(--muted)}
.copyright b{color:var(--accent);font-weight:400}
.social{position:absolute;left:902px;top:333px;display:flex;gap:15px}
.social span{width:22px;height:22px;border-radius:50%;background:#fff;display:block}
.to-top{position:absolute;left:1158px;top:3126px;width:30px;height:30px;border-radius:50%;background:var(--ink);display:flex;align-items:center;justify-content:center}
</style>
</head>
<body>

<div class="topbar">
  <div class="contact-item" style="left:161px">
    <div class="ico"><svg width="11" height="11" viewBox="0 0 24 24" fill="#fff"><path d="M6.6 10.8a15 15 0 006.6 6.6l2.2-2.2c.3-.3.7-.4 1-.2 1.1.4 2.3.6 3.6.6.6 0 1 .4 1 1V20c0 .6-.4 1-1 1A17 17 0 013 4c0-.6.4-1 1-1h3.5c.6 0 1 .4 1 1 0 1.3.2 2.5.6 3.6.1.3 0 .7-.2 1z"/></svg></div>
    <div><b>Free Call:</b><span>+00 5550 128 304</span></div>
  </div>
  <div class="contact-item" style="left:296px">
    <div class="ico">@</div>
    <div><b>Email Us:</b><span>mail@harlowvectors.example</span></div>
  </div>
  <div class="contact-item" style="left:492px">
    <div class="ico"><svg width="10" height="12" viewBox="0 0 24 30" fill="#fff"><path d="M12 0a11 11 0 00-11 11c0 8 11 19 11 19s11-11 11-19A11 11 0 0012 0zm0 15a4 4 0 110-8 4 4 0 010 8z"/></svg></div>
    <div><b>Visit Us:</b><span>14 Fenwick Row, Cambridge</span></div>
  </div>
  <div class="client-login">Client Login <svg width="10" height="10" viewBox="0 0 10 10"><path d="M1 5h7M5 2l3 3-3 3" stroke="#fff" stroke-width="1.4" fill="none"/></svg></div>
</div>

<header class="header">
  <div class="brand"><i></i>Harlow Vectors</div>
  <nav class="nav"><span>Home</span><span>About Us</span><span>Hiring</span><span>Press Release</span><span>Contact Us</span></nav>
</header>

<section class="hero">
  <div class="hero-net" role="img" aria-label="Faint network of connected nodes"></div>
  <h1>Bringing AI and Statistical Inference to Financial Markets</h1>
  <p>Harlow Vectors is a quantitative asset manager with the singular focus of delivering algorithmic strategies that work.</p>
  <div class="btn btn-dark" style="left:161px;top:332px;width:88px;height:38px">Get Hired</div>
  <div class="btn btn-light" style="left:273px;top:332px;width:100px;height:38px">What we do</div>
  <div class="vertical-url">WWW.HARLOWVECTORS.EXAMPLE</div>
</section>

<div class="photo" style="left:161px;top:650px;width:375px;height:313px;background:linear-gradient(135deg,#8fa3b6,#dfe5ea 55%,#a9b7c4)" role="img" aria-label="Tablet showing financial charts over a desk with market figures"></div>
<div class="kicker" style="left:612px;top:663px">About Us</div>
<h2 class="title" style="left:612px;top:683px">Our Values &amp; Approach</h2>
<div class="dash" style="left:612px;top:740px"></div>
<div class="copy" style="left:612px;top:772px">
  <p>We deliver consistent alpha across liquid markets through the application of proprietary IP in Bayesian inference, machine learning and artificial intelligence. We are a multi-disciplinary team founded by experienced finance professionals from premier institutions, leading academics from the Thornbury Stellar Unit at Ashmere College and world-class software engineers.</p>
  <p>Our logo portrays a sillhoute of the lattice walkway at Ashmere College. Our unique scientific approach allows us to bridge cutting-edge mathematical research and computing expertise with financial knowledge to bring algorithmns that work to liquid markets</p>
</div>

<div class="photo" style="left:161px;top:1087px;width:375px;height:314px;background:linear-gradient(135deg,#2c3d55,#8896a6 50%,#d5dbe1)" role="img" aria-label="Business handshake over a desk"></div>
<div class="kicker" style="left:612px;top:1101px">Hiring</div>
<h2 class="title" style="left:612px;top:1121px">Exceptional Talent Search</h2>
<div class="dash" style="left:612px;top:1178px"></div>
<div class="copy" style="left:612px;top:1209px">
  <p>We are always looking for exceptional talent to join our entrepreneurial team. We are looking for individuals who are creative thinkers, can demonstrate analytical rigour and are passionate about the intersection of science, finance and technology.</p>
  <p>We prioritise having a company culture that promotes sharing ideas in a safe, collaborative research environment. We make sure that every member of the team has the oppertunity to explore their own ideas through weekly 'innovation time', and ensure that everyone gets the support they need to continue to grow as individuals within the company.</p>
</div>

<section class="press">
  <div class="press-net" role="img" aria-label="Faint network of connected nodes"></div>
  <div class="kicker">News</div>
  <h2>Latest Press Releases</h2>
  <div class="card-img" style="left:161px;background:linear-gradient(135deg,#c9cdd1,#7d8590 60%,#4a5058)" role="img" aria-label="Hands using a tablet on a desk"></div>
  <div class="card-img" style="left:461px;background:linear-gradient(135deg,#c7a57c,#3d6ea8 50%,#5a4636)" role="img" aria-label="Tablet displaying bar and pie charts"></div>
  <div class="card-img" style="left:761px;background:linear-gradient(135deg,#dfe5ec,#a7b5c5 55%,#5c6c80)" role="img" aria-label="Hand touching a rising growth chart"></div>
  <article class="card" style="left:191px"><h3>Role Of Technology</h3><time>Aug 27 2021</time><div class="shares"><span></span><span></span><span></span><span></span></div></article>
  <article class="card" style="left:491px"><h3>AI Role in Finance</h3><time>Aug 28 2021</time><div class="shares"><span></span><span></span><span></span><span></span></div></article>
  <article class="card" style="left:791px"><h3>Growth Through AI</h3><time>Aug 29 2021</time><div class="shares"><span></span><span></span><span></span><span></span></div></article>
</section>

<div class="section-label">Contact Us</div>
<h2 class="contact-title">Get In Touch</h2>
<div class="field" style="left:237px;top:2232px;width:351px;height:37px">Your Name *</div>
<div class="field" style="left:610px;top:2232px;width:353px;height:37px">Your Email *</div>
<div class="field" style="left:237px;top:2283px;width:351px;height:37px">Your Phone *</div>
<div class="field select" style="left:610px;top:2283px;width:353px;height:37px"><span>I Would Like to Discuss</span><span>&#8661;</span></div>
<div class="field" style="left:237px;top:2336px;width:726px;height:186px">Your Message *</div>
<div class="btn btn-dark" style="left:534px;top:2538px;width:130px;height:41px">Send Message <svg width="10" height="10" viewBox="0 0 10 10"><path d="M1 5h7M5 2l3 3-3 3" stroke="#fff" stroke-width="1.4" fill="none"/></svg></div>

<section class="cta">
  <h2>Looking for Bringing AI and Statistical Inference to Financial Markets?</h2>
  <div class="btn">Request a Quote <svg width="10" height="10" viewBox="0 0 10 10"><path d="M1 5h7M5 2l3 3-3 3" stroke="#fff" stroke-width="1.4" fill="none"/></svg></div>
</section>

<footer class="offices">
  <div class="office" style="left:199px">
    <div class="pin"><svg width="14" height="18" viewBox="0 0 24 30" fill="#0d3e6e"><path d="M12 0a11 11 0 00-11 11c0 8 11 19 11 19s11-11 11-19A11 11 0 0012 0zm0 15a4 4 0 110-8 4 4 0 010 8z"/></svg></div>
    <h3>Cambridge</h3>
    <p>212 Orchard Lane, Westvale<br>ZX 40213, Cambridge<br>+5550-204718 - Office<br>+5550-204718 - Fax<br>support@harlowvectors.example</p>
  </div>
  <div class="office" style="left:480px">
    <div class="pin"><svg width="14" height="18" viewBox="0 0 24 30" fill="#0d3e6e"><path d="M12 0a11 11 0 00-11 11c0 8 11 19 11 19s11-11 11-19A11 11 0 0012 0zm0 15a4 4 0 110-8 4 4 0 010 8z"/></svg></div>
    <h3>London</h3>
    <p>212 Orchard Lane, Westvale<br>QL 70219, London<br>+5550-204718 - Office<br>+5550-204718 - Fax<br>support@harlowvectors.example</p>
  </div>
  <div class="office" style="left:760px">
    <div class="pin"><svg width="14" height="18" viewBox="0 0 24 30" fill="#0d3e6e"><path d="M12 0a11 11 0 00-11 11c0 8 11 19 11 19s11-11 11-19A11 11 0 0012 0zm0 15a4 4 0 110-8 4 4 0 010 8z"/></svg></div>
    <h3>Singapore</h3>
    <p>212 Orchard Lane, Westvale<br>VP 30418, Singapore<br>+5550-204718 - Office<br>+5550-204718 - Fax<br>support@harlowvectors.example</p>
  </div>
  <div class="rule"></div>
  <div class="copyright">2021 © <b>harlowvectors</b>. All rights reserved.</div>
  <div class="social"><span></span><span></span><span></span><span></span></div>
</footer>
<div class="to-top"><svg width="10" height="10" viewBox="0 0 10 10"><path d="M2 6l3-3 3 3M2 9l3-3 3 3" stroke="#fff" stroke-width="1.3" fill="none"/></svg></div>

</body>
</html>
```